Dune Air & Plus business card

I need an awesome, double-sided business card designed with our new logo. I would like the one side black with the colored logo, and the back side is all yours. I'd like to see horizontal and vertical layouts. Get creative! Thank you.

Target Market(s)

HVAC, Heating and Cooling in Phoenix, AZ

Industry/Entity Type

HVAC

Contact Information for Business Card

We need our new logo on the card. Tom Harker, (623) 555-0142, tom@trydunesair.com, www.trydunesair.com, ROC 514273

```html
<!DOCTYPE html>
<html lang="en">
<head>
<meta charset="utf-8">
<title>Dune Air &amp; Plus — Business Card</title>
<link rel="stylesheet" href="https://fonts.googleapis.com/css2?family=Archivo+Black&family=Arimo:wght@400&display=swap">
<style>
  :root {
    --backdrop: #2b2b2d;
    --card-black: #171717;
    --brand-blue: #1d7fe0;
    --brand-orange: #f47b20;
    --blue-light: #0b72d4;
    --blue-deep: #03489f;
    --emboss: #1a7ee0;
    --white: #ffffff;
  }
  * { margin: 0; padding: 0; box-sizing: border-box; }
  html, body { width: 1200px; height: 1015px; overflow: hidden; }
  body {
    background: var(--backdrop);
    display: flex;
    flex-direction: column;
    align-items: center;
    justify-content: center;
    gap: 55px;
  }
  .card {
    width: 700px;
    height: 400px;
    position: relative;
    box-shadow: 0 14px 30px rgba(0,0,0,0.55);
    overflow: hidden;
  }
  .card--front {
    background: var(--card-black);
    display: flex;
    align-items: center;
    justify-content: center;
  }
  .brand-lockup {
    display: flex;
    align-items: center;
    gap: 18px;
  }
  .brand-dot {
    width: 34px; height: 34px;
    border-radius: 50%;
    background: var(--brand-orange);
  }
  .brand-name {
    font-family: "Archivo Black", sans-serif;
    font-size: 46px;
    color: var(--brand-blue);
    letter-spacing: 1px;
    text-transform: uppercase;
  }
  .card--back {
    background: linear-gradient(160deg, var(--blue-light) 0%, var(--blue-deep) 100%);
  }
  .contact-block {
    position: absolute;
    left: 70px;
    top: 105px;
  }
  .person-name {
    font-family: "Archivo Black", sans-serif;
    font-size: 30px;
    color: var(--brand-orange);
    text-transform: uppercase;
    letter-spacing: 1px;
    margin-bottom: 26px;
  }
  .contact-list { list-style: none; }
  .contact-item {
    display: flex;
    align-items: center;
    gap: 10px;
    font-family: "Arimo", sans-serif;
    font-size: 19px;
    color: var(--white);
    line-height: 30px;
  }
  .contact-icon { width: 17px; height: 17px; flex: none; }
  .licence {
    margin-top: 44px;
    font-family: "Arimo", sans-serif;
    font-size: 21px;
    color: var(--white);
  }
  .licence-label { color: var(--brand-orange); margin-right: 6px; }
  .emboss-name {
    position: absolute;
    right: 40px;
    top: 120px;
    width: 300px;
    font-family: "Archivo Black", sans-serif;
    font-size: 50px;
    line-height: 1.05;
    color: var(--emboss);
    text-transform: uppercase;
    text-align: center;
  }
</style>
</head>
<body>
  <section class="card card--front" aria-label="Card front">
    <div class="brand-lockup">
      <span class="brand-dot"></span>
      <span class="brand-name">Dune Air &amp; Plus</span>
    </div>
  </section>

  <section class="card card--back" aria-label="Card back">
    <div class="contact-block">
      <h1 class="person-name">Tom Harker</h1>
      <ul class="contact-list">
        <li class="contact-item">
          <svg class="contact-icon" viewBox="0 0 24 24"><path fill="#f47b20" d="M6.6 10.8a15.2 15.2 0 0 0 6.6 6.6l2.2-2.2a1 1 0 0 1 1-.25 11.4 11.4 0 0 0 3.6.57 1 1 0 0 1 1 1V20a1 1 0 0 1-1 1A17 17 0 0 1 3 4a1 1 0 0 1 1-1h3.5a1 1 0 0 1 1 1c0 1.25.2 2.45.57 3.57a1 1 0 0 1-.25 1z"/></svg>
          (623) 555-0142
        </li>
        <li class="contact-item">
          <svg class="contact-icon" viewBox="0 0 24 24"><rect x="2" y="5" width="20" height="14" fill="#f47b20"/><path d="M2 5l10 8 10-8" fill="none" stroke="#03489f" stroke-width="2"/></svg>
          tom@trydunesair.com
        </li>
        <li class="contact-item">
          <svg class="contact-icon" viewBox="0 0 24 24" fill="none" stroke="#f47b20" stroke-width="2"><circle cx="12" cy="12" r="10"/><ellipse cx="12" cy="12" rx="4.5" ry="10"/><path d="M2 12h20M4 7h16M4 17h16"/></svg>
          www.trydunesair.com
        </li>
      </ul>
      <p class="licence"><span class="licence-label">ROC</span>514273</p>
    </div>
    <div class="emboss-name">Dune Air &amp; Plus</div>
  </section>
</body>
</html>
```